New boutique hotel for tourists, with hint of art deco styling

This is a new, soon to be completed, boutique hotel in Sydney. A letterhead with a logo is required. Less emphasis on the word "boutique". Perhaps the word could be screened to be lighter in colour (or print intensity). Would like a simple, clear, easy-to read, sans serif type face. The information on the letterhead is:
Mrs Fennel Boutique Hotel
417 Larkmoor Street,
Wellbrook, NSW, 2094
Australia
Tel: +61 2 9704-5512
mrsfennelhotel@example-mail.com
mrsfennelhotel.example.au
ABN 47 902 365 148

Target Market(s)

travellers, tourists, various ages

Industry/Entity Type

Hospitality

Contact Information for Business Card

Mrs Fennel Boutique Hotel
417 Larkmoor Street,
Wellbrook, NSW, 2097
Telephone: (02) 9704-5512
www.mrsfennelhotel.example.au
mrsfennelhotel@example-mail.com
ABN 47 902 365 148

Logo Text

suggest playing with the letter "B"

Font styles to use
Sans Serif

Colors
3176b5

Requirements
Must have
• ABN to be very small.
• Must be clear, easy to read and in a sans serif typeface, please!
Nice to have
• The word "Boutique" should be less intense in appearance to the rest of the name, or even "Boutique Hotel" can have less prominence than "Mrs Fennel".
Should not have
• No serif typeface. Sans serif only will be accepted.

```html
<!DOCTYPE html>
<html lang="en">
<head>
<meta charset="utf-8">
<title>Mrs Fennel Boutique Hotel — Business Card</title>
<link rel="stylesheet" href="https://fonts.googleapis.com/css2?family=Jost:wght@400&display=swap">
<style>
  :root {
    --navy: #03243f;
    --paper: #ffffff;
    --backdrop: #b9b9b9;
    --ink: #03243f;
  }
  * { box-sizing: border-box; margin: 0; padding: 0; }
  html, body {
    width: 1200px; height: 1200px; overflow: hidden;
    background: var(--backdrop);
    font-family: "Jost", sans-serif;
  }
  .card {
    position: absolute;
    left: 346px;
    width: 508px;
    background: var(--paper);
    overflow: hidden;
  }
  .card--front { top: 256px; height: 294px; }
  .card--back  { top: 636px; height: 300px; }

  .hotel-name {
    font-weight: 400;
    white-space: nowrap;
    line-height: 1;
  }

  /* Front */
  .front-band {
    position: absolute; left: 0; top: 72px; width: 100%; height: 150px;
    background: var(--navy);
    display: flex; align-items: center; justify-content: center;
  }
  .front-band .hotel-name {
    color: var(--paper);
    font-size: 30px;
    letter-spacing: 0.5px;
  }
  .front-url {
    position: absolute; left: 0; right: 0; top: 248px;
    text-align: center;
    font-size: 8.5px; letter-spacing: 5px;
    color: var(--ink);
  }

  /* Back */
  .back-bands { position: absolute; left: 0; top: 0; width: 508px; height: 300px; }
  .back-name {
    position: absolute; left: 34px; top: 146px;
    color: var(--ink);
    font-size: 17px;
    letter-spacing: 0.2px;
  }
  .contact {
    position: absolute; left: 302px; top: 100px;
    list-style: none;
    color: var(--ink);
    font-size: 12px; line-height: 14px;
  }
  .contact li { display: flex; align-items: flex-start; gap: 7px; }
  .contact svg { flex: none; width: 9px; height: 9px; margin-top: 2.5px; }
  .abn {
    position: absolute; left: 0; right: 0; top: 246px;
    text-align: center;
    font-size: 12px; letter-spacing: 5px;
    color: var(--ink);
  }
</style>
</head>
<body>

<section class="card card--front">
  <div class="front-band">
    <p class="hotel-name">Mrs Fennel Boutique Hotel</p>
  </div>
  <p class="front-url">mrsfennelhotel.example.au</p>
</section>

<section class="card card--back">
  <svg class="back-bands" viewBox="0 0 508 300" aria-hidden="true">
    <polygon points="0,13 300,13 312,35 0,35" fill="var(--navy)"/>
    <polygon points="307,13 508,13 508,35 319,35" fill="var(--navy)"/>
    <polygon points="0,274 312,274 300,295 0,295" fill="var(--navy)"/>
    <polygon points="319,274 508,274 508,295 307,295" fill="var(--navy)"/>
  </svg>

  <p class="hotel-name back-name">Mrs Fennel Boutique Hotel</p>

  <ul class="contact">
    <li>
      <svg viewBox="0 0 10 10"><rect width="10" height="10" rx="2" fill="var(--navy)"/><path d="M2.5 5.2 5 3l2.5 2.2V7.5h-5z" fill="#fff"/></svg>
      <span>417 Larkmoor Street,<br>Wellbrook,<br>Sydney, NSW 2097<br>Australia</span>
    </li>
    <li>
      <svg viewBox="0 0 10 10"><rect width="10" height="10" rx="2" fill="var(--navy)"/><path d="M3 2.5c.6 2.6 1.9 3.9 4.5 4.5l-.6-1.3-1.2.3C5 5.4 4.6 5 4.2 4.3l.3-1.2z" fill="#fff"/></svg>
      <span>+61 2 9704-5512</span>
    </li>
    <li>
      <svg viewBox="0 0 10 10"><rect width="10" height="10" rx="2" fill="var(--navy)"/><rect x="2.2" y="3" width="5.6" height="4" fill="none" stroke="#fff" stroke-width=".8"/><path d="M2.2 3 5 5.3 7.8 3" fill="none" stroke="#fff" stroke-width=".8"/></svg>
      <span>mrsfennelhotel@example-mail.com</span>
    </li>
    <li>
      <svg viewBox="0 0 10 10"><rect width="10" height="10" rx="2" fill="var(--navy)"/><circle cx="5" cy="5" r="2.6" fill="none" stroke="#fff" stroke-width=".8"/><path d="M2.4 5h5.2M5 2.4v5.2" stroke="#fff" stroke-width=".6"/></svg>
      <span>mrsfennelhotel.example.au</span>
    </li>
  </ul>

  <p class="abn">ABN 47 902 365 148</p>
</section>

</body>
</html>
```